Business Cards for Tax Preparation Business
KRT Tax Preparation
Business Cards for Tax Preparation Business - Financial Services
Creative Brief
Cutting-Edge
Brian K Holloway
Registered Tax Return Preparer
47 Birchmont Avenue, Suite 318 Maple Falls, NH 03299
603-555-0148 x36
brian@krtfiling.example
www.krtfiling.example

```html
<!DOCTYPE html>
<html lang="en">
<head>
<meta charset="utf-8">
<title>KRT Tax Preparation – Business Cards</title>
<link href="https://fonts.googleapis.com/css2?family=Open+Sans:wght@400;600;700&display=swap" rel="stylesheet">
<style>
  :root{
    --page:#e6e8ec;
    --blue:#2a5cb8;
    --blue-dark:#1d3f94;
    --blue-light:#4f7fd6;
    --ink-grey:#7d7f86;
    --card-white:#ffffff;
    --card-fade:#eef0f4;
  }
  *{margin:0;padding:0;box-sizing:border-box}
  html,body{width:1200px;height:898px;overflow:hidden}
  body{background:var(--page);font-family:"Open Sans",Arial,sans-serif;position:relative}

  .card{position:absolute;width:700px;height:400px;border-radius:22px;overflow:hidden;
        box-shadow:0 10px 26px rgba(0,0,0,.18)}

  /* back */
  .card-back{left:250px;top:28px;
    background:radial-gradient(ellipse at 45% 40%,var(--blue-light) 0%,var(--blue) 45%,var(--blue-dark) 100%)}
  .card-back .brand{position:absolute;left:0;right:0;top:150px;text-align:center;color:#fff}
  .card-back .brand-name{font-size:40px;font-weight:700;display:inline-flex;align-items:center;gap:16px}
  .card-back .brand-dot{width:34px;height:34px;border-radius:50%;background:#fff;display:inline-block}
  .card-back .web{position:absolute;right:70px;bottom:46px;color:#fff;font-size:19px;font-weight:600}

  /* front */
  .card-front{left:250px;top:468px;
    background:linear-gradient(160deg,var(--card-white) 0%,var(--card-white) 55%,var(--card-fade) 100%)}
  .card-front .brand{position:absolute;left:48px;top:40px;display:flex;align-items:center;gap:12px;
    color:var(--blue);font-size:30px;font-weight:700}
  .card-front .brand-dot{width:26px;height:26px;border-radius:50%;background:var(--blue)}
  .side-tab{position:absolute;left:0;top:150px;width:12px;height:40px;background:var(--blue)}
  .person{position:absolute;left:48px;top:150px}
  .person .name{color:var(--blue);font-size:24px;font-weight:600}
  .person .title{color:var(--ink-grey);font-size:14px;margin-top:2px}

  .contact{position:absolute;left:400px;top:145px;color:var(--ink-grey);font-size:15px}
  .contact .address{color:var(--blue);font-size:17px;font-weight:600;line-height:1.25;margin-bottom:8px}
  .contact ul{list-style:none}
  .contact li{display:flex;align-items:center;gap:10px;line-height:22px}
  .contact svg{width:15px;height:15px;fill:var(--blue)}
  .contact .web{color:var(--blue);font-size:18px;font-weight:700;margin-top:6px}

  .bands{position:absolute;left:0;bottom:0;width:700px;height:56px}
</style>
</head>
<body>

<section class="card card-back" aria-label="Card back">
  <div class="brand"><span class="brand-name"><span class="brand-dot"></span>KRT Tax Preparation</span></div>
  <div class="web">www.krtfiling.example</div>
</section>

<section class="card card-front" aria-label="Card front">
  <div class="brand"><span class="brand-dot"></span>KRT Tax Preparation</div>

  <div class="side-tab"></div>
  <div class="person">
    <div class="name">Brian K Holloway</div>
    <div class="title">Registered Tax Return Preparer</div>
  </div>

  <div class="contact">
    <div class="address">47 Birchmont Avenue, Suite 318<br>Maple Falls, NH 03299</div>
    <ul>
      <li><svg viewBox="0 0 16 16"><path d="M3 1h3l1 4-2 1a9 9 0 0 0 5 5l1-2 4 1v3a2 2 0 0 1-2 2A13 13 0 0 1 1 3a2 2 0 0 1 2-2z"/></svg>603-555-0148 x36</li>
      <li><svg viewBox="0 0 16 16"><rect x="4" y="1" width="8" height="5"/><rect x="1" y="6" width="14" height="6" rx="1"/><rect x="4" y="10" width="8" height="5"/></svg>603-555-0172</li>
      <li><svg viewBox="0 0 16 16"><rect x="4" y="0" width="8" height="16" rx="1.5"/></svg>603-555-0193</li>
      <li><svg viewBox="0 0 16 16"><path d="M1 3h14v10H1z M1 3l7 6 7-6" stroke="#fff" stroke-width="1"/></svg>brian@krtfiling.example</li>
    </ul>
    <div class="web">www.krtfiling.example</div>
  </div>

  <svg class="bands" viewBox="0 0 700 56" preserveAspectRatio="none">
    <path d="M0 12 Q350 0 700 12 L700 56 L0 56Z" fill="var(--blue-light)" opacity=".55"/>
    <path d="M0 22 Q350 10 700 22 L700 56 L0 56Z" fill="var(--blue)"/>
    <path d="M0 38 Q350 28 700 38 L700 56 L0 56Z" fill="var(--blue-dark)"/>
  </svg>
</section>

</body>
</html>
```